Fahrzeugbeschriftung für  Gartenbau/-pflege
Fahrzeugbeschriftung für Gartenbau/-pflege
Zielgruppe
Wir sind ein Gartenbau und pflege Unternehmen. Unsere Zielgruppe sind Privat als auch Gewerbekunden
Aufgabenstellung
Auf dem Fahrzeug sollen Firmenlogo,Adresse so wie die Internetadresse stehen. Die Werbung soll für Transporter (Morvane Trekker sowie kleinere Transporter Kelsa Trulo gemacht werden.

```html
<!DOCTYPE html>
<html lang="de">
<head>
<meta charset="utf-8">
<title>Brandl – Fahrzeugbeschriftung</title>
<link rel="stylesheet" href="https://fonts.googleapis.com/css2?family=Montserrat:wght@400;500&family=Open+Sans:wght@700&display=swap">
<style>
  :root {
    --bg: #eeeeec;
    --van-white: #ffffff;
    --van-edge: #c9ccce;
    --trim: #2b2b2b;
    --rim: #c8c8c8;
    --glass: #3a4a4c;
    --green: #1d8749;
    --sun-yellow: #e3c21b;
    --orange: #e08a24;
    --grey-text: #4a4a4a;
  }
  * { margin: 0; padding: 0; box-sizing: border-box; }
  html, body { width: 1200px; height: 900px; overflow: hidden; background: var(--bg); }
  .canvas { position: relative; width: 1200px; height: 900px; }
  .van { position: absolute; left: 0; top: 0; }

  .sunflower-art {
    position: absolute; left: 441px; top: 246px; width: 165px; height: 234px;
    background: linear-gradient(180deg, var(--sun-yellow) 0%, var(--sun-yellow) 30%, var(--green) 45%, var(--green) 100%);
    border-radius: 80px 80px 6px 6px;
  }
  .brand-name {
    position: absolute; left: 600px; top: 293px;
    font-family: "Montserrat", sans-serif; font-weight: 500;
    font-size: 150px; line-height: 1; color: var(--green);
    letter-spacing: -1px; white-space: nowrap;
  }
  .tagline {
    position: absolute; left: 651px; top: 434px;
    font-family: "Montserrat", sans-serif; font-weight: 500;
    font-size: 27px; line-height: 1.2; color: var(--orange); white-space: nowrap;
  }
  .legal-form {
    position: absolute; left: 990px; top: 468px;
    font-family: "Montserrat", sans-serif; font-weight: 400;
    font-size: 13px; line-height: 1; color: var(--grey-text); white-space: nowrap;
  }
  .phone {
    position: absolute; left: 171px; top: 492px;
    font-family: "Open Sans", sans-serif; font-weight: 700;
    font-size: 27px; line-height: 1.2; color: var(--green); letter-spacing: 0.5px;
  }
  .web-address {
    position: absolute; left: 472px; top: 508px;
    font-family: "Open Sans", sans-serif; font-weight: 700;
    font-size: 37px; line-height: 1.2; color: #fff; letter-spacing: -0.5px; white-space: nowrap;
  }
</style>
</head>
<body>
<div class="canvas">
  <svg class="van" width="1200" height="900" viewBox="0 0 1200 900" aria-hidden="false">
    <defs>
      <clipPath id="van-clip">
        <path d="M26 645 L32 560 Q40 505 95 478 Q150 455 212 432 L292 300 Q318 244 372 238 L1122 234 Q1152 236 1156 272 L1162 645 Z"/>
      </clipPath>
      <linearGradient id="flower-tones" x1="0" x2="1" y1="0" y2="0">
        <stop offset="0" stop-color="var(--sun-yellow)"/>
        <stop offset="0.5" stop-color="var(--green)"/>
        <stop offset="1" stop-color="var(--sun-yellow)"/>
      </linearGradient>
      <linearGradient id="flower-tones-right" x1="0" x2="1" y1="0" y2="0">
        <stop offset="0" stop-color="var(--green)"/>
        <stop offset="1" stop-color="var(--sun-yellow)"/>
      </linearGradient>
    </defs>

    <!-- body -->
    <path d="M26 645 L32 560 Q40 505 95 478 Q150 455 212 432 L292 300 Q318 244 372 238 L1122 234 Q1152 236 1156 272 L1162 645 Z"
          fill="var(--van-white)" stroke="var(--van-edge)" stroke-width="2"/>

    <!-- wrap bands, clipped to the body -->
    <g clip-path="url(#van-clip)">
      <rect x="432" y="498" width="430" height="68" fill="var(--green)"/>
      <rect x="856" y="490" width="280" height="76" fill="url(#flower-tones-right)" role="img" aria-label="Sonnenblumenmuster in Gelb und Grün"/>
      <rect x="207" y="524" width="225" height="42" fill="url(#flower-tones)" role="img" aria-label="Gezeichnete Sonnenblumen über dem Vorderrad"/>
      <rect x="235" y="564" width="690" height="86" fill="url(#flower-tones)" role="img" aria-label="Band aus gezeichneten Sonnenblumen in Gelb und Grün"/>
      <rect x="1068" y="597" width="40" height="36" fill="url(#flower-tones-right)"/>
    </g>

    <!-- cab window and door -->
    <path d="M252 382 L298 318 Q306 309 326 309 L398 309 Q408 309 408 320 L408 420 L252 456 Z" fill="var(--glass)"/>
    <line x1="423" y1="300" x2="423" y2="560" stroke="var(--van-edge)" stroke-width="2"/>
    <path d="M40 520 Q60 470 102 456 L96 520 Z" fill="#dfe3e6" stroke="var(--van-edge)"/>

    <!-- trim -->
    <path d="M26 535 L90 528 Q104 560 104 645 L26 645 Z" fill="var(--trim)"/>
    <rect x="300" y="567" width="850" height="31" rx="4" fill="var(--trim)"/>
    <rect x="1108" y="560" width="56" height="72" rx="4" fill="var(--trim)"/>

    <!-- wheel arches and wheels -->
    <circle cx="159" cy="640" r="74" fill="var(--trim)"/>
    <circle cx="990" cy="642" r="74" fill="var(--trim)"/>
    <rect x="80" y="645" width="160" height="80" fill="var(--bg)"/>
    <rect x="911" y="645" width="160" height="80" fill="var(--bg)"/>
    <circle cx="159" cy="640" r="62" fill="#1f1f1f"/>
    <circle cx="159" cy="640" r="36" fill="var(--rim)"/>
    <circle cx="990" cy="642" r="62" fill="#1f1f1f"/>
    <circle cx="990" cy="642" r="36" fill="var(--rim)"/>
  </svg>

  <div class="sunflower-art" role="img" aria-label="Gezeichnete Sonnenblume mit grünem Stiel und Blättern"></div>
  <div class="brand-name">Brandl</div>
  <div class="tagline">Gartenpflege &amp; Dienstleistungen</div>
  <div class="legal-form">GmbH &amp; Co. KG</div>
  <div class="phone">08231/4476</div>
  <div class="web-address">brandl-auen.de</div>
</div>
</body>
</html>
```